Laundry Hamper Assembly Instruction Manual

We are looking for an easy to understand design to update the existing instruction manual. Attached are the current instructions. These instructions are too basic

Please visit the company website for design colors and ideas:
http://www.quilvaware.com/

And the Zarvello detail page of the product:
https://www.zarvello.com/Heavy-Canvas-Laundry-Hamper-Casters/dp/K482R7WXMD/ref=sr_1_1?s=home-garden&ie=UTF8&qid=1620384915&sr=1-1&keywords=K482R7WXMD
Updates

Project Deadline Extended Reason: Submitting more time so designers have the ability to supply project that include the instructions for the product.Thank you!! Added Monday, August 7, 2017

Target Market(s)

Purchasers of home products

Colors

Designer to choose colors to be used in the design.

Requirements
Must have
• Quilva logo
• Assembly instructions
• At the bottom it needs to state" For help assembling this product, or if you find that parts are missing, please contact our customer service department at 1-800-316-2740 Monday through Friday 8am-5pm CST or e-mail us at quilvainfo@quilvaware.com
• Para obtener ayuda para ensamblar este producto, o si le faltan piezas, llame a nuestra linea de atencion al cliente 1-800-316-2740 de lunes a viernes de 8am-5pm CST o escribanos por cor reo eletronico en quilvainfo@quilvaware.com"
• We need two versions one in color and one in and black and white please.
Nice to have
• Please use the website for colors and font. http://www.quilvaware.com/
• Needs to be simple but completely show how to assemble the product.

```html
<!DOCTYPE html>
<html lang="en">
<head>
<meta charset="utf-8">
<title>Quilva Laundry Hamper – Instruction Sheets</title>
<link rel="stylesheet" href="https://fonts.googleapis.com/css2?family=Ubuntu:ital,wght@0,300;0,400;0,500;0,700;1,300;1,400&display=swap">
<style>
  :root{
    --page-bg:#ecebe8;
    --paper:#ffffff;
    --ink:#555555;
    --ink-soft:#666666;
    --brand-blue:#1a86b8;
    --brand-green:#8dc63f;
    --mono-dark:#77787a;
    --mono-mid:#8e8f91;
    --mono-light:#a7a8aa;
    --rule:#9aa3a8;
  }
  *{box-sizing:border-box;margin:0;padding:0}
  html,body{width:1200px;height:751px;overflow:hidden}
  body{background:var(--page-bg);font-family:"Ubuntu",sans-serif;color:var(--ink);position:relative}

  .sheet{position:absolute;top:50px;width:507px;height:655px;background:var(--paper);
    box-shadow:0 2px 8px rgba(0,0,0,.18);overflow:hidden;
    --accent:var(--brand-blue);--heading:var(--brand-blue);--footer:var(--brand-green);--label:var(--brand-blue);--ink-body:#555}
  .sheet--color{left:57px}
  .sheet--mono{left:628px;--accent:var(--mono-dark);--heading:#666;--footer:var(--mono-light);--label:#6a6a6a;--ink-body:#777}

  .sheet__header{position:absolute;left:0;top:0;width:100%;height:85px;background:var(--accent)}
  .sheet__title{position:absolute;left:28px;top:26px;font-size:27px;font-weight:400;color:#fff;letter-spacing:.2px}
  .brand{position:absolute;left:369px;top:17px;width:121px;height:55px;background:#fff;border:2px solid #1a1a1a;
    border-radius:2px;display:flex;align-items:center;justify-content:center;
    font-size:30px;font-weight:500;color:#1a1a1a;letter-spacing:-.5px}

  .photo{position:absolute;border-radius:0}
  .photo--main{left:30px;top:134px;width:207px;height:205px;
    background:linear-gradient(160deg,#efece2 0%,#dedad0 60%,#cfcbc1 100%);border-radius:4px}
  .sheet--mono .photo--main{background:linear-gradient(160deg,#e6e7e8 0%,#d2d3d5 60%,#c2c3c5 100%)}
  .detail{position:absolute;top:356px;width:66px;height:66px;border-radius:50%;border:1px solid #d9d9d9;
    background:radial-gradient(circle at 40% 40%,#f1eee6,#d6d1c5)}
  .sheet--mono .detail{background:radial-gradient(circle at 40% 40%,#eeeeef,#cfd0d2)}
  .detail--wheel{left:22px}.detail--inside{left:100px}.detail--snaps{left:181px}

  .product{position:absolute;left:271px;top:127px;width:230px}
  .product__name{font-size:23px;font-weight:400;color:var(--heading)}
  .product__size{font-size:9.5px;font-weight:300;margin-top:3px;color:var(--ink-body)}
  .product__rule{width:205px;height:1px;background:var(--rule);margin-top:6px}
  .features{list-style:none;margin-top:9px;font-size:10px;font-weight:300;line-height:15.7px;color:var(--ink-body)}
  .features li{position:relative;padding-left:11px}
  .features li::before{content:"";position:absolute;left:0;top:5px;width:5px;height:5px;border-radius:50%;
    border:1.5px solid #9a9a9a;background:#fff}

  .highlights{position:absolute;left:271px;top:351px;width:236px;height:75px;background:var(--accent);
    color:#fff;list-style:none;font-size:9.3px;font-weight:400;line-height:15.7px;padding:6px 0 0 10px}
  .sheet--mono .highlights{font-weight:300}
  .highlights li::before{content:"• "}

  .notice{position:absolute;left:16px;top:460px;width:228px;text-align:center;font-size:9.3px;font-weight:700;
    line-height:11px;color:var(--label)}
  .review{position:absolute;left:16px;top:504px;width:230px;font-size:6.4px;font-style:italic;font-weight:300;
    line-height:9.2px;color:var(--ink-body)}
  .review__stars{color:#f3b400;font-style:normal;font-size:7px;letter-spacing:.5px;line-height:8px}
  .sheet--mono .review__stars{color:#bdbdbd}

  .diagram{position:absolute}
  .diagram--frame{left:296px;top:464px;width:88px;height:97px;
    background:linear-gradient(180deg,#f7f7f7,#e9e9e9);border:1px solid #d5d5d5}
  .diagram--bag{left:392px;top:451px;width:75px;height:108px;
    background:linear-gradient(180deg,#f1f1f1,#dcdcdc);border:1px solid #cfcfcf}
  .step-arrow{position:absolute;left:358px;top:432px;width:76px;height:36px}

  .footer-rule{position:absolute;left:0;top:578px;width:100%;height:3px;background:var(--accent)}
  .sheet--color .footer-rule{background:var(--brand-blue)}
  .sheet__footer{position:absolute;left:0;top:584px;width:100%;height:71px;background:var(--footer);color:#fff;
    text-align:center;font-size:8.2px;font-weight:400;line-height:10px;padding-top:12px}
  .sheet--mono .sheet__footer{font-weight:300}
  .sheet__footer p + p{margin-top:5px}
  .sheet__footer b{font-weight:700}
</style>
</head>
<body>

<article class="sheet sheet--color">
  <header class="sheet__header">
    <h1 class="sheet__title">Laundry Hamper</h1>
    <div class="brand">quilva</div>
  </header>

  <div class="photo photo--main" role="img" aria-label="Photo of the canvas industrial hamper on its metal frame with casters"></div>

  <section class="product">
    <h2 class="product__name">Industrial Hamper</h2>
    <p class="product__size">size: 22″x 17″x 24″</p>
    <div class="product__rule"></div>
    <ul class="features">
      <li>100% Cotton</li>
      <li>Imported</li>
      <li>Strong cotton canvas laundry bag<br>supports up to 5 loads of laundry.</li>
      <li>Sturdy metal frame adds strength;<br>button snaps allow easy attachment&nbsp; of canvas<br>bag to frame.</li>
      <li>Heavy duty casters and long handles make it<br>easy to move the hamper, even when full</li>
    </ul>
  </section>

  <div class="detail detail--wheel" role="img" aria-label="Close-up of a locking caster wheel"></div>
  <div class="detail detail--inside" role="img" aria-label="Hamper filled with laundry"></div>
  <div class="detail detail--snaps" role="img" aria-label="Close-up of button snaps on the canvas bag"></div>

  <ul class="highlights">
    <li>Strong canvas bag snaps onto sturdy metal frame</li>
    <li>Large straps for portability</li>
    <li>Industrial style locking wheels</li>
    <li>Holds 5 loads of laundry</li>
  </ul>

  <p class="notice">Please fallow instructions carefully before assembly<br>Siga las instrucciones con atención antes de armar</p>

  <div class="review">
    <div class="review__stars">★★★★★</div>
    “Easy to move!<br>
    This hamper is large and holds a good amount of laundry. It's very easy to move from my laundry shoot over to the washer. The unit was pretty easy to put together, the hardest part was getting some of the buttons as the sides are pretty taught. But the end result was looks really great!”- Dana
  </div>

  <svg class="step-arrow" viewBox="0 0 76 36" aria-hidden="true">
    <path d="M6 30 Q36 -6 68 26" fill="none" stroke="#222" stroke-width="2"/>
    <path d="M62 22 L70 30 L71 19" fill="none" stroke="#222" stroke-width="2"/>
  </svg>
  <div class="diagram diagram--frame" role="img" aria-label="Line drawing of the empty metal hamper frame"></div>
  <div class="diagram diagram--bag" role="img" aria-label="Line drawing of the canvas bag snapped onto the frame"></div>

  <div class="footer-rule"></div>
  <footer class="sheet__footer">
    <p>For help assembling this product, or if you find that parts are missing, please contact our customer service department at<br><b>1-800-316-2740</b> Monday through Friday 8am-5pm CST or e-mail us at <b>quilvainfo@quilvaware.com</b></p>
    <p>Para obtener ayuda para ensamblar este producto, o si le faltan piezas, llame a nuestra linea de atencion al cliente<br><b>1-800-316-2740</b> de lunes a viernes de 8am-5pm CST o escribanos por cor reo eletronico en <b>quilvainfo@quilvaware.com</b></p>
  </footer>
</article>

<article class="sheet sheet--mono">
  <header class="sheet__header">
    <h1 class="sheet__title">Laundry Hamper</h1>
    <div class="brand">quilva</div>
  </header>

  <div class="photo photo--main" role="img" aria-label="Greyscale photo of the canvas industrial hamper on its metal frame with casters"></div>

  <section class="product">
    <h2 class="product__name">Industrial Hamper</h2>
    <p class="product__size">size: 22″x 17″x 24″</p>
    <div class="product__rule"></div>
    <ul class="features">
      <li>100% Cotton</li>
      <li>Imported</li>
      <li>Strong cotton canvas laundry bag<br>supports up to 5 loads of laundry.</li>
      <li>Sturdy metal frame adds strength;<br>button snaps allow easy attachment&nbsp; of canvas<br>bag to frame.</li>
      <li>Heavy duty casters and long handles make it<br>easy to move the hamper, even when full</li>
    </ul>
  </section>

  <div class="detail detail--wheel" role="img" aria-label="Greyscale close-up of a locking caster wheel"></div>
  <div class="detail detail--inside" role="img" aria-label="Greyscale view of the hamper filled with laundry"></div>
  <div class="detail detail--snaps" role="img" aria-label="Greyscale close-up of button snaps on the canvas bag"></div>

  <ul class="highlights">
    <li>Strong canvas bag snaps onto sturdy metal frame</li>
    <li>Large straps for portability</li>
    <li>Industrial style locking wheels</li>
    <li>Holds 5 loads of laundry</li>
  </ul>

  <p class="notice">Please fallow instructions carefully before assembly<br>Siga las instrucciones con atención antes de armar</p>

  <div class="review">
    <div class="review__stars">★★★★★</div>
    “Easy to move!<br>
    This hamper is large and holds a good amount of laundry. It's very easy to move from my laundry shoot over to the washer. The unit was pretty easy to put together, the hardest part was getting some of the buttons as the sides are pretty taught. But the end result was looks really great!”- Dana
  </div>

  <svg class="step-arrow" viewBox="0 0 76 36" aria-hidden="true">
    <path d="M6 30 Q36 -6 68 26" fill="none" stroke="#222" stroke-width="2"/>
    <path d="M62 22 L70 30 L71 19" fill="none" stroke="#222" stroke-width="2"/>
  </svg>
  <div class="diagram diagram--frame" role="img" aria-label="Line drawing of the empty metal hamper frame"></div>
  <div class="diagram diagram--bag" role="img" aria-label="Line drawing of the canvas bag snapped onto the frame"></div>

  <div class="footer-rule"></div>
  <footer class="sheet__footer">
    <p>For help assembling this product, or if you find that parts are missing, please contact our customer service department at<br><b>1-800-316-2740</b> Monday through Friday 8am-5pm CST or e-mail us at <b>quilvainfo@quilvaware.com</b></p>
    <p>Para obtener ayuda para ensamblar este producto, o si le faltan piezas, llame a nuestra linea de atencion al cliente<br><b>1-800-316-2740</b> de lunes a viernes de 8am-5pm CST o escribanos por cor reo eletronico en <b>quilvainfo@quilvaware.com</b></p>
  </footer>
</article>

</body>
</html>
```